Maplecrest Apartments Downtown Northport

We are looking to redesign our entry way sign at Maplecrest Apartments, a low density residential apartment building, located in Downtown Northport, Alabama, U.S. Downtown Northport is a bustling boutique business district with a small town feel comprised of shops, restaurants, and a renowned arts community known for Varrow Arts Center and Festival which is one of the nation's top outdoor arts festivals. Maplecrest Apartments and its sign is the first thing you seen when you enter Downtown Northport. We are looking to redesign our sign, entry way and landscaping to compliment the building and character of the historic downtown.

Target Market(s)

Our apartment building is comprised of 20 apartments units with tenants who are primarily part of the local workforce, young professionals, or students at the Halverton College or other nearby institutions.

Requirements
Must have
• The name of the apartment building - Maplecrest
Phone number on the sign 205-555-0148

```html
<!DOCTYPE html>
<html lang="en">
<head>
<meta charset="utf-8">
<title>Maplecrest Apartments – Entry Sign Options</title>
<link rel="stylesheet" href="https://fonts.googleapis.com/css2?family=Rye&family=Oswald:wght@400&display=swap">
<style>
  :root {
    --gold-light: #e0c983;
    --gold-mid: #d4b96c;
    --gold-deep: #c6a85a;
    --sign-dark: #000000;
    --sign-light: #ffffff;
    --page: #ffffff;
  }
  html, body {
    margin: 0;
    padding: 0;
    width: 1200px;
    height: 1000px;
    overflow: hidden;
    background: var(--page);
  }
  .sign-board {
    display: block;
    width: 1200px;
    height: 1000px;
  }
  .sign-name {
    font-family: "Rye", serif;
    font-size: 128px;
  }
  .sign-name .initial {
    font-size: 150px;
  }
  .sign-type {
    font-family: "Rye", serif;
    font-size: 38px;
  }
  .sign-phone {
    font-family: "Oswald", sans-serif;
    font-size: 36px;
  }
</style>
</head>
<body>
<svg class="sign-board" viewBox="0 0 1200 1000" xmlns="http://www.w3.org/2000/svg">
  <defs>
    <linearGradient id="gold" x1="0" y1="0" x2="1" y2="0">
      <stop offset="0" stop-color="var(--gold-deep)"/>
      <stop offset="0.5" stop-color="var(--gold-mid)"/>
      <stop offset="1" stop-color="var(--gold-light)"/>
    </linearGradient>
  </defs>

  <!-- Dark version -->
  <g class="sign sign--dark">
    <rect class="sign-frame" x="113" y="82" width="971" height="386" fill="url(#gold)"/>
    <rect class="sign-field" x="129" y="98" width="939" height="354" fill="var(--sign-dark)"/>
    <rect class="sign-inner-rule" x="141.5" y="110.5" width="915" height="329" fill="none" stroke="url(#gold)" stroke-width="2"/>
    <text class="sign-name" x="210" y="272" textLength="760" lengthAdjust="spacingAndGlyphs" fill="url(#gold)"><tspan class="initial">M</tspan>APLECREST</text>
    <rect class="sign-divider" x="232" y="289" width="736" height="4" fill="url(#gold)"/>
    <text class="sign-type" x="607" y="352" text-anchor="middle" textLength="355" lengthAdjust="spacingAndGlyphs" fill="url(#gold)">APARTMENTS</text>
    <text class="sign-phone" x="603" y="404" text-anchor="middle" textLength="278" lengthAdjust="spacingAndGlyphs" fill="url(#gold)">-205 555 0148-</text>
  </g>

  <!-- Light version -->
  <g class="sign sign--light">
    <rect class="sign-frame" x="121" y="537" width="971" height="385" fill="url(#gold)"/>
    <rect class="sign-field" x="137" y="553" width="939" height="353" fill="var(--sign-light)"/>
    <rect class="sign-inner-rule" x="150.5" y="566.5" width="912" height="326" fill="none" stroke="url(#gold)" stroke-width="2"/>
    <text class="sign-name" x="218" y="726" textLength="760" lengthAdjust="spacingAndGlyphs" fill="url(#gold)"><tspan class="initial">M</tspan>APLECREST</text>
    <rect class="sign-divider" x="241" y="744" width="736" height="4" fill="url(#gold)"/>
    <text class="sign-type" x="616" y="808" text-anchor="middle" textLength="355" lengthAdjust="spacingAndGlyphs" fill="url(#gold)">APARTMENTS</text>
    <text class="sign-phone" x="611" y="861" text-anchor="middle" textLength="278" lengthAdjust="spacingAndGlyphs" fill="url(#gold)">-205 555 0148-</text>
  </g>
</svg>
</body>
</html>
```